Exclusive Social Networking Platform for future CEOs (no coding required)

We need a creative remake design (from rough mock-ups) for our social networking platform. We are a US-based start-up company called Kindred Lumora. Our platform allows high-caliber students and young professionals that are part of established networks to reconnect online. It also has an element of Wanderloft.com (host exchange system). In terms of the layout, it can therefore be considered a combination of:
- Tallyvine (CV style profiles)
- Glimmerly (messaging, pictures, posts, etc.)
- Wanderloft

UPDATE: We have been asking a few people to try to implement a map of the world (maybe just the outlines) as a backdrop to the platform, but in such a way that it is only faintly noticeable and doesn't become distracting to the platform.

If we really like your designs we may approach you for future designs for a collection of other businesses on a freelance basis (we work out of an incubator).

CONDITIONS: We are only asking for 2 pages as examples (attached PDFs). There may be an opportunity for you to design the rest of the platform as well.

Thank you very much for your designs so far! There are some very good ones among them. 

Reason: We are still waiting on several designers to provide their edited versions, and we have not yet found the designs we are looking for.

Target Market(s)

Our users are:
1. high-potential global students and young professionals
2. that have been selected to participate in high-end conferences & networks
3. and are typically entrepreneurs, techies, or young corporates
4. they love to travel
5. they are very ambitious about their careers
6. they spend a lot of time meeting people and networking

Industry/Entity Type

It Company

Requirements
Must have
• Base colours (can contain any combination of the following—you can also exclude blue if you like):
- Dark grey (almost black)
- lighter greys
- white
- blue

In terms of the design, please base it on the functional layouts we have provided (attached files). Feel free to redesign as you wish (both in colour and structure), as long as it keeps the functionality outlined by the rough sketches.
- please redesign the icons at the top (News Feed, Events, Pellora, Expeditions) to a very simple and attractive format

NOTE: Please provide one design for each of the 2 PDF files ('Quiltra' and 'Profile') to show us how you creatively visualise the platform ('Quiltra' is the most up-to-date version considering the icons on the top and the general layout). Please also consider the attached logo to get a feeling of our brand.
Nice to have
• We would be happy to see a creative infusion of the colourful colours of our logo (see attached file). With this, it would be important that it would be kept to a minimum (as otherwise it will be distracting), so a good place to include it may be in the icons that direct people around the site, or in other parts that are more creative—up to you!

```html
<!DOCTYPE html>
<html lang="en">
<head>
<meta charset="utf-8">
<title>Kindred Lumora – My Wall</title>
<link rel="stylesheet" href="https://fonts.googleapis.com/css2?family=Arimo:wght@400;700&display=swap">
<style>
:root{
  --navy:#1b4660;
  --banner:#1d4a86;
  --orange:#f07a1c;
  --ink:#1f4a66;
  --text:#555;
  --muted:#8a9aa6;
  --rule:#7f9bb0;
  --green:#3f8f3a;
  --dot-orange:#f26d21;
  --footer:#cfcfcf;
  --white:#fff;
}
*{box-sizing:border-box;margin:0;padding:0}
html,body{width:1200px;height:780px;overflow:hidden}
body{position:relative;background:var(--white);font-family:"Arimo",Arial,sans-serif;color:var(--text)}
.abs{position:absolute}

/* top bar */
.topbar{left:0;top:0;width:1200px;height:46px;background:var(--navy)}
.brand{left:18px;top:7px;display:flex;align-items:center;gap:8px}
.brand-dot{width:32px;height:32px;border-radius:50%;background:var(--white)}
.brand-name{color:var(--white);font-size:17px;letter-spacing:.3px}
.search{left:238px;top:11px;width:308px;height:25px;background:var(--white);border:none;font-size:13px;color:#9aa;padding:5px 8px;font-family:inherit}
.mainnav{left:580px;top:10px;width:372px;height:66px;background:var(--white);border-radius:3px;display:flex;justify-content:space-around;padding:8px 6px 0}
.navitem{display:flex;flex-direction:column;align-items:center;gap:4px;font-size:11px;color:#4a7390}
.navitem svg{width:32px;height:32px}
.usertools{left:984px;top:0;width:216px;height:46px;background:var(--orange);display:flex;align-items:center;justify-content:center;gap:20px}
.usertools svg{width:20px;height:20px}

/* left column */
.col-title{font-size:19px;color:var(--ink)}
.mynet{left:22px;top:80px}
.network-list{left:20px;top:110px;width:190px;list-style:none}
.network-list li{display:flex;align-items:flex-start;gap:10px;height:42px;font-size:12.5px;color:#333;line-height:13px}
.net-thumb{width:42px;height:38px;flex:none}
.divider{left:19px;top:297px;width:193px;height:2px;background:#f3b57d}
.chat-search{left:21px;top:309px;width:180px;height:25px;border:1px solid #bbb;font-size:12px;color:#9bb;padding:5px 10px;font-family:inherit}
.chat-list{left:21px;top:345px;list-style:none}
.chat-list li{position:relative;height:44px;display:flex;gap:10px;font-size:12.5px;color:#333}
.avatar{width:42px;height:40px;flex:none}
.status{position:absolute;left:52px;top:24px;width:9px;height:9px;border-radius:50%}
.on{background:var(--green)}.away{background:var(--dot-orange)}

/* wall */
.wall-title{left:230px;top:80px}
.banner{left:217px;top:107px;width:765px;height:177px;background:linear-gradient(100deg,#1a4381,#2356a0 55%,#1b4583)}
.portrait{left:230px;top:120px;width:136px;height:152px;border:3px solid var(--white);border-radius:4px;background:linear-gradient(160deg,#8a6a55,#c9a48c 55%,#6e6a5e)}
.profile-facts{left:380px;top:127px;list-style:none;color:var(--white)}
.profile-facts li{height:30px;display:flex;align-items:baseline;gap:9px}
.profile-facts b{font-size:18px}
.profile-facts span{font-size:13px;color:#c5d3e6}
.tabs{left:580px;top:253px;width:372px;height:31px;background:var(--white);border-radius:3px 3px 0 0;display:flex;gap:26px;padding:13px 0 0 28px;font-size:11.5px;color:#6b8aa0}
.summary-head{left:236px;top:309px;width:720px;font-size:17px;color:var(--ink);padding-bottom:6px;border-bottom:1px solid var(--rule)}
.summary{left:238px;top:351px;width:700px;font-size:11.5px;line-height:12.5px;color:#666}
.summary p+p{margin-top:24px}
.sections{left:236px;top:525px;width:720px;list-style:none}
.sections li{height:37.5px;padding-top:2px;font-size:17px;color:var(--ink);border-bottom:1px solid var(--rule)}

/* right column */
.events-title{left:997px;top:78px}
.events{left:996px;top:115px;list-style:none;width:190px}
.events li{height:97px}
.event-name{font-size:12.5px;color:#333;margin-bottom:6px}
.event-row{display:flex;gap:8px}
.event-thumb{width:64px;height:58px;flex:none}
.event-text{font-size:12.5px;line-height:12.5px;color:#555}

/* chat popup + footer */
.chatpop{left:952px;top:716px;width:216px;height:36px;background:var(--navy);display:flex;align-items:center;padding:0 10px;color:var(--white);font-size:13px;gap:8px}
.chatpop .close{margin-left:auto;color:#9fb3c4;font-size:14px}
.chatpop .dot{width:9px;height:9px;border-radius:50%;background:var(--green)}
.footer{left:0;top:753px;width:1200px;height:27px;background:var(--footer);border-top:2px solid var(--orange)}
</style>
</head>
<body>

<header class="abs topbar"></header>
<div class="abs brand"><span class="brand-dot"></span><span class="brand-name">Kindred Lumora</span></div>
<input class="abs search" value="search for people, places or networks" aria-label="Search">

<nav class="abs mainnav">
  <div class="navitem">
    <svg viewBox="0 0 32 32" fill="none" stroke="#1f4a66" stroke-width="2"><rect x="7" y="3" width="18" height="26" rx="1" fill="#1f4a66"/><path d="M11 9h10M11 13h10M11 17h10M11 21h7" stroke="#fff"/></svg>News Feed</div>
  <div class="navitem">
    <svg viewBox="0 0 32 32"><rect x="4" y="5" width="24" height="24" rx="2" fill="none" stroke="#1f4a66" stroke-width="2.4"/><rect x="4" y="5" width="24" height="6" fill="#1f4a66"/><path d="M10 2v6M22 2v6" stroke="#1f4a66" stroke-width="2.4"/><text x="16" y="25" text-anchor="middle" font-size="12" font-weight="700" fill="#1f4a66" font-family="Arimo,Arial,sans-serif">17</text></svg>Event</div>
  <div class="navitem">
    <svg viewBox="0 0 32 32" stroke="#444" stroke-width="1.3"><path d="M6 8L16 16L26 5M16 16L10 27M16 16L27 24M6 8L10 27"/><circle cx="6" cy="8" r="3" fill="#e43d3d"/><circle cx="26" cy="5" r="3" fill="#f2a91b"/><circle cx="16" cy="16" r="3" fill="#3a8fd6"/><circle cx="10" cy="27" r="3" fill="#4caf50"/><circle cx="27" cy="24" r="3" fill="#8e44ad"/></svg>Networks</div>
  <div class="navitem">
    <svg viewBox="0 0 32 32" fill="none" stroke="#1f4a66" stroke-width="1.8"><circle cx="16" cy="16" r="13"/><ellipse cx="16" cy="16" rx="6" ry="13"/><path d="M3 16h26M5 9h22M5 23h22"/></svg>Pellora</div>
  <div class="navitem">
    <svg viewBox="0 0 32 32" fill="none" stroke="#1f4a66" stroke-width="2.4"><circle cx="16" cy="16" r="12"/><path d="M16 2v9M16 21v9M2 16h9M21 16h9"/></svg>Expenditons</div>
</nav>

<div class="abs usertools">
  <svg viewBox="0 0 20 20" fill="#fff"><circle cx="7" cy="6" r="3"/><circle cx="14" cy="6" r="3"/><path d="M1 17c0-4 3-6 6-6s6 2 6 6zM12 11c3 0 7 1 7 6h-4"/></svg>
  <svg viewBox="0 0 20 20" fill="#fff"><path d="M1 2h12v8H5l-4 3z"/><path d="M15 6h4v9l-3-2H8v-2h7z"/></svg>
  <svg viewBox="0 0 20 20" fill="#fde0c7"><circle cx="10" cy="6" r="4"/><path d="M3 19c0-5 3-7 7-7s7 2 7 7z"/></svg>
  <svg viewBox="0 0 20 20" fill="#fff"><circle cx="10" cy="10" r="6"/><circle cx="10" cy="10" r="2.5" fill="#f07a1c"/><path d="M9 1h2v4H9zM9 15h2v4H9zM1 9h4v2H1zM15 9h4v2h-4z"/></svg>
</div>

<!-- left column -->
<h2 class="abs col-title mynet">My Network</h2>
<ul class="abs network-list">
  <li><span class="net-thumb" role="img" aria-label="Global Venture Forum network badge" style="background:#e6eaef"></span>Global Venture<br>Forum</li>
  <li><span class="net-thumb" role="img" aria-label="Aurelis network badge" style="background:#f2ede3"></span>Aurelis</li>
  <li><span class="net-thumb" role="img" aria-label="Brightmark network badge" style="background:#f7e4ef"></span>Brightmark</li>
  <li><span class="net-thumb" role="img" aria-label="Southern Trade Circle network badge" style="background:#e8f0e3"></span>Southern Trade<br>Circle</li>
</ul>
<div class="abs divider"></div>
<input class="abs chat-search" value="search chat" aria-label="Search chat">
<ul class="abs chat-list">
  <li><span class="avatar" role="img" aria-label="Profile photo of Tobias Reyn" style="background:#b08a72"></span>Tobias Reyn<span class="status on"></span></li>
  <li><span class="avatar" role="img" aria-label="Profile photo of Elian" style="background:#6f4a3e"></span>Elian<span class="status on"></span></li>
  <li><span class="avatar" role="img" aria-label="Profile photo of Samuel Orne" style="background:#5a5046"></span>Samuel Orne<span class="status on"></span></li>
  <li><span class="avatar" role="img" aria-label="Profile photo of Tobias Reyn" style="background:#8c6d67"></span>Tobias Reyn<span class="status away"></span></li>
  <li><span class="avatar" role="img" aria-label="Profile photo of Elian" style="background:#6d6f72"></span>Elian<span class="status away"></span></li>
  <li><span class="avatar" role="img" aria-label="Profile photo of Samuel Orne" style="background:#8f8378"></span>Samuel Orne<span class="status away"></span></li>
</ul>

<!-- wall -->
<h2 class="abs col-title wall-title">My Wall</h2>
<section class="abs banner" role="img" aria-label="Profile banner with faint network backdrop"></section>
<div class="abs portrait" role="img" aria-label="Profile photo of Ravi Castellan Moor"></div>
<ul class="abs profile-facts">
  <li><b>Ravi Castellan Moor</b><span>Co founder at Kindred Lumora &amp; Northwind Atelier</span></li>
  <li><b>Mission in life</b><span>turning acquaintances into friendships &amp; saving the rainforests</span></li>
  <li><b>Based in</b><span>Conterbury, UK</span></li>
  <li><b>Current Location</b><span>Conterbury, UK</span></li>
</ul>
<nav class="abs tabs"><span>CV</span><span>About Me</span><span>Host &amp; Travel</span><span>Photos</span></nav>

<h3 class="abs summary-head">Professinal Summary</h3>
<div class="abs summary">
  <p>Lorem Ipsum is simply dummy text of the printing and typesetting industry. Lorem Ipsum has been the industry's standard dummy text ever since the 1500s, when an unknown printer took a galley of type and scrambled it to make a type specimen book. It has survived not only five centuries, but also the leap into electronic typesetting, remaining essentially unchanged.</p>
  <p>It was popularised in the 1960s with the release of Typeline sheets containing Lorem Ipsum passages, and more recently with desktop publishing software like Folio Press including versions of Lorem Ipsum.</p>
</div>
<ul class="abs sections">
  <li>Work Experience</li>
  <li>Key Soft Skills</li>
  <li>Key Technical Skills</li>
  <li>Languages</li>
  <li>Social Network</li>
</ul>

<!-- right column -->
<h2 class="abs col-title events-title">Events &amp; Deadlines</h2>
<ul class="abs events">
  <li><div class="event-name">Global Venture Forum</div><div class="event-row"><span class="event-thumb" role="img" aria-label="Event image" style="background:linear-gradient(#2c8fc6,#7fc14a)"></span><span class="event-text">Easy to create. Free hosting. Live support when you need it.</span></div></li>
  <li><div class="event-name">Global Venture Forum</div><div class="event-row"><span class="event-thumb" role="img" aria-label="Event photo collage" style="background:linear-gradient(#5a4a48,#b9a7a4)"></span><span class="event-text">Easy to create. Free hosting. Live support when you need it.</span></div></li>
  <li><div class="event-name">Global Venture Forum</div><div class="event-row"><span class="event-thumb" role="img" aria-label="Event image" style="background:radial-gradient(circle,#c8262c 30%,#f3eeee 70%)"></span><span class="event-text">Easy to create. Free hosting. Live support when you need it.</span></div></li>
  <li><div class="event-name">Global Venture Forum</div><div class="event-row"><span class="event-thumb" role="img" aria-label="Event image" style="background:#1d4a86"></span><span class="event-text">Easy to create. Free hosting. Live support when you need it.</span></div></li>
</ul>

<div class="abs chatpop"><span class="dot"></span>Tobias Reyn<span class="close">x</span></div>
<footer class="abs footer"></footer>

</body>
</html>
```